Melissa Dorvan Personal Business Card

I like orange. It's would better if my card have an orange background
Address: 5820 Halvers Lane #417
San Jose
California
US
Tel: 4085172049

Industry/Entity Type

Business

```html
<!DOCTYPE html>
<html lang="en">
<head>
<meta charset="UTF-8">
<title>Melissa Dorvan – Business Card</title>
<link rel="stylesheet" href="https://fonts.googleapis.com/css2?family=Jost:wght@400;500&display=swap">
<style>
  :root {
    --page: #ffffff;
    --orange-deep: #ec5a12;
    --orange: #f3861c;
    --amber: #f6a823;
    --yellow: #f7cb22;
    --yellow-soft: #f8d64a;
    --ink: #111111;
    --strip: #ffffff;
  }
  * { margin: 0; padding: 0; box-sizing: border-box; }
  html, body {
    width: 1200px;
    height: 738px;
    overflow: hidden;
    background: var(--page);
  }
  .canvas {
    position: relative;
    width: 1200px;
    height: 738px;
    background: var(--page);
  }
  .card {
    position: absolute;
    left: 62px;
    top: 57px;
    width: 1076px;
    height: 616px;
    overflow: hidden;
  }
  .card__backdrop {
    position: absolute;
    inset: 0;
    background:
      linear-gradient(125deg, transparent 55%, rgba(236, 90, 18, 0.55) 100%),
      linear-gradient(180deg,
        var(--orange) 0%,
        var(--orange) 22%,
        var(--amber) 34%,
        var(--yellow) 52%,
        var(--amber) 72%,
        var(--yellow-soft) 100%);
  }
  .card__name {
    position: absolute;
    left: 0;
    right: 0;
    top: 310px;
    text-align: center;
    font-family: "Jost", sans-serif;
    font-weight: 500;
    font-size: 82px;
    line-height: 1;
    color: var(--ink);
    letter-spacing: 0.5px;
  }
  .card__contact {
    position: absolute;
    left: 0;
    right: 0;
    top: 542px;
    height: 68px;
    background: var(--strip);
    display: flex;
    align-items: center;
    justify-content: center;
    font-family: "Jost", sans-serif;
    font-weight: 400;
    font-size: 29px;
    color: var(--ink);
    white-space: nowrap;
  }
  .card__contact .sep { margin: 0 12px; }
</style>
</head>
<body>
  <div class="canvas">
    <div class="card">
      <div class="card__backdrop" role="img" aria-label="Orange and yellow geometric triangle pattern background"></div>
      <h1 class="card__name">Melissa Dorvan</h1>
      <p class="card__contact">
        <span>5820 Halvers Lane #417</span><span class="sep">|</span><span>San Jose, California US</span><span class="sep">|</span><span>Tel: 4085172049</span>
      </p>
    </div>
  </div>
</body>
</html>
```